Sticker design for prepared meals

I need 3 separate sticker designs for 3 categories of food - all of prepared meal types.
1. Traditional - needs to reflect traditional food/baking of old days Think rustic old style cooking. Maybe a checked table cloth. Maybe a sketch of someone baking with an oven etc.Needs to include our existing logo and wording "Ferdie's Traditional House Made Meals"
2. Takeaway - needs to reflect choice from popular takeaway cuisines - eg Chinese, Thai, Indian, Japanese. Needs to highlight choice - eg family of 4 can get what they want - not all the same cuisine etc. Words " Every family member gets to choose - top quality house made takeaway"
3. Fine Dining - needs to be classy and premium - eg black background with gold lettering - very pristine' very classy. Words include" Ferdie's Fine Dining at your home"
These will be for 3 separate types of stickers 80mm x 30 mm and I will need all files etc to pass onto the sticker company. Thanks

People interested in buying quality food and busy.

• As per project description

```html
<!DOCTYPE html>
<html lang="en">
<head>
<meta charset="utf-8">
<title>Ferdie's Prepared Meal Stickers</title>
<link rel="stylesheet" href="https://fonts.googleapis.com/css2?family=Arimo:wght@400;700&family=Cinzel:wght@400&family=Great+Vibes&family=Montserrat:ital,wght@0,400;0,500;0,800;1,400&family=Yesteryear&display=swap">
<style>
  :root {
    --page: #ffffff;
    --ink: #111111;
    --orange: #ff9a00;
    --orange-deep: #d96f00;
    --orange-band: #f2b300;
    --banner-red: #ff1a00;
    --maroon: #5c0b0b;
    --red: #ff0d0d;
    --red-deep: #d40000;
    --yellow: #ffd23a;
    --white: #ffffff;
    --shadow: #4a0000;
    --wine: #2e0202;
    --wine-soft: #1f0101;
    --gold: #c9961e;
    --navy: #2f2a6e;
  }
  * { box-sizing: border-box; margin: 0; padding: 0; }
  html, body { width: 1200px; height: 1000px; overflow: hidden; background: var(--page); }
  .canvas { position: relative; width: 1200px; height: 1000px; }

  .category-label {
    position: absolute; left: 40px; width: 216px; text-align: center;
    font-family: "Arimo", Arial, sans-serif; color: var(--ink);
  }
  .category-label .number { display: block; font-weight: 700; font-size: 42px; line-height: 42px; }
  .category-label .name { display: block; font-size: 34px; line-height: 38px; }

  .sticker {
    position: absolute; left: 265px; width: 760px; height: 284px;
    border-radius: 16px; overflow: hidden;
  }
  .sticker--traditional { top: 55px; background: var(--orange); }
  .sticker--takeaway { top: 368px; background: var(--red); }
  .sticker--fine { top: 680px; background: var(--wine); }

  .tablecloth-band { position: absolute; left: 0; width: 100%; height: 58px; background: var(--orange-band); opacity: .55; }
  .tablecloth-band--top { top: 0; }
  .tablecloth-band--bottom { bottom: 0; }

  .decor { position: absolute; }

  .store-mark {
    position: absolute; left: 26px; top: 82px; width: 250px; height: 120px;
    display: flex; align-items: center; gap: 12px;
  }
  .store-mark .dot { flex: 0 0 40px; height: 40px; border-radius: 50%; background: var(--navy); }
  .store-mark .store-name {
    font-family: "Montserrat", sans-serif; font-weight: 800; font-size: 28px;
    line-height: 32px; color: var(--navy);
  }
  .sticker--takeaway .store-mark .store-name { color: var(--white); }
  .sticker--fine .store-mark .store-name { color: var(--gold); }
  .sticker--takeaway .store-mark .dot { background: var(--white); }
  .sticker--fine .store-mark .dot { background: var(--gold); }

  /* Traditional */
  .tag-line {
    position: absolute; left: 349px; top: 28px; padding: 0 10px; height: 38px;
    background: var(--banner-red); color: var(--white);
    font-family: "Montserrat", sans-serif; font-weight: 500; font-size: 28px; line-height: 38px;
  }
  .script-title {
    position: absolute; left: 280px; top: 70px; width: 470px; text-align: center;
    font-family: "Yesteryear", cursive; color: var(--maroon); font-size: 92px; line-height: 96px;
    text-shadow: -2px -2px 0 var(--white), 2px -2px 0 var(--white), -2px 2px 0 var(--white), 2px 2px 0 var(--white), 4px 5px 0 var(--shadow);
  }

  /* Takeaway */
  .cuisine-list { position: absolute; left: 284px; top: 18px; width: 70px; list-style: none; }
  .cuisine { height: 64px; display: flex; flex-direction: column; align-items: center; }
  .cuisine .box { width: 30px; height: 30px; background: var(--white); position: relative; }
  .cuisine .box svg { position: absolute; left: -2px; top: -10px; }
  .cuisine .label { margin-top: 6px; font-family: "Montserrat", sans-serif; font-size: 12px; color: var(--white); }
  .choose-line {
    position: absolute; left: 390px; top: 18px; width: 320px; text-align: center;
    font-family: "Montserrat", sans-serif; font-style: italic; font-size: 23px; line-height: 26px; color: var(--yellow);
  }
  .quality-line {
    position: absolute; left: 410px; top: 84px; width: 300px; text-align: center;
    font-family: "Montserrat", sans-serif; font-weight: 500; font-size: 28px; line-height: 30px; color: var(--white);
  }
  .takeaway-title {
    position: absolute; left: 360px; top: 146px; width: 400px; text-align: center;
    font-family: "Montserrat", sans-serif; font-weight: 800; font-size: 55px; line-height: 56px; color: var(--white);
    text-shadow: 4px 4px 0 var(--shadow);
  }

  /* Fine dining */
  .fine-name, .fine-sub {
    position: absolute; left: 330px; width: 370px; text-align: center;
    font-family: "Cinzel", serif; color: var(--white);
  }
  .fine-name { top: 22px; font-size: 40px; line-height: 48px; }
  .fine-sub { top: 210px; font-size: 42px; line-height: 50px; }
  .fine-title {
    position: absolute; left: 280px; top: 90px; width: 470px; text-align: center;
    font-family: "Great Vibes", cursive; color: var(--gold); font-size: 82px; line-height: 100px;
  }
</style>
</head>
<body>
<main class="canvas">

  <p class="category-label" style="top:180px"><span class="number">1.</span><span class="name">Traditional</span></p>
  <p class="category-label" style="top:462px"><span class="number">2.</span><span class="name">Takeaway</span></p>
  <p class="category-label" style="top:762px"><span class="number">3.</span><span class="name">Fine Dining</span></p>

  <section class="sticker sticker--traditional">
    <div class="tablecloth-band tablecloth-band--top" role="img" aria-label="Checked tablecloth band"></div>
    <div class="tablecloth-band tablecloth-band--bottom" role="img" aria-label="Checked tablecloth band"></div>
    <div class="decor" role="img" aria-label="Wooden spoon illustration" style="left:270px;top:72px;width:460px;height:180px;border-radius:90px;background:var(--orange-deep);opacity:.45"></div>
    <div class="store-mark"><span class="dot"></span><span class="store-name">Ferdie's Fresh Pantry</span></div>
    <p class="tag-line">Ferdie's Traditional</p>
    <h2 class="script-title">House Made<br>Meals</h2>
  </section>

  <section class="sticker sticker--takeaway">
    <div class="decor" role="img" aria-label="Cutlery and takeaway tray illustration" style="left:350px;top:70px;width:380px;height:200px;border-radius:30px;background:var(--red-deep);opacity:.6"></div>
    <div class="store-mark"><span class="dot"></span><span class="store-name">Ferdie's Fresh Pantry</span></div>
    <ul class="cuisine-list">
      <li class="cuisine"><span class="box"></span><span class="label">CHINESE</span></li>
      <li class="cuisine"><span class="box"></span><span class="label">THAI</span></li>
      <li class="cuisine"><span class="box"><svg width="36" height="40" viewBox="0 0 36 40" aria-hidden="true"><path d="M6 24 L14 33 L32 6" fill="none" stroke="#111" stroke-width="5" stroke-linecap="square"/></svg></span><span class="label">JAPANESE</span></li>
      <li class="cuisine"><span class="box"></span><span class="label">INDIAN</span></li>
    </ul>
    <p class="choose-line">EVERY FAMILY MEMBER<br>GETS TO CHOOSE -</p>
    <p class="quality-line">Top Quality<br>House</p>
    <h2 class="takeaway-title">MADE<br>TAKEAWAY</h2>
  </section>

  <section class="sticker sticker--fine">
    <div class="decor" role="img" aria-label="Serving cloche silhouette" style="left:355px;top:60px;width:330px;height:180px;border-radius:165px 165px 10px 10px;background:var(--wine-soft)"></div>
    <div class="store-mark"><span class="dot"></span><span class="store-name">Ferdie's Fresh Pantry</span></div>
    <p class="fine-name">Ferdie's</p>
    <h2 class="fine-title">Fine Dining</h2>
    <p class="fine-sub">AT YOUR HOME</p>
  </section>

</main>
</body>
</html>
```